Bref créative
Overseas Capital Partners
I need single sided standard sized Business Card [3.5" x 2"]
May be same as in logo, may be another
Professional
Marek Dobrzyn
Manager
ul. Lipowa 17
41-806 Harlow
Estovia
marek.dobrzyn@korvant.com.pl
www.korvant.com.pl

```html
<!DOCTYPE html>
<html lang="en">
<head>
<meta charset="utf-8">
<title>Overseas Capital Partners – Business Cards</title>
<link href="https://fonts.googleapis.com/css2?family=Arimo:wght@400;700&display=swap" rel="stylesheet">
<style>
  :root {
    --bg: #e7e4df;
    --white-card: #f6f7f8;
    --white-card-edge: #e2e5e8;
    --dark-card: #1b1d20;
    --dark-card-edge: #2c2f33;
    --brand-blue: #2aa7e0;
    --brand-light: #7fd0f2;
    --brand-pale: #d6eefa;
    --text-dark: #3a3d42;
    --text-light: #d9dde2;
    --muted-dark: #6b7078;
    --muted-light: #9aa1a9;
  }
  * { margin: 0; padding: 0; box-sizing: border-box; }
  html, body { width: 1200px; height: 911px; overflow: hidden; }
  body {
    background: var(--bg);
    font-family: "Arimo", Arial, sans-serif;
    position: relative;
  }
  .card {
    position: absolute;
    width: 500px;
    height: 286px;
    border-radius: 10px;
    overflow: hidden;
    box-shadow: 0 6px 18px rgba(0,0,0,.18);
  }
  .card--white { background: linear-gradient(160deg, #ffffff 0%, var(--white-card) 55%, var(--white-card-edge) 100%); }
  .card--dark { background: linear-gradient(160deg, var(--dark-card-edge) 0%, var(--dark-card) 60%, #121316 100%); }
  .card--front-white { left: 70px; top: 140px; }
  .card--front-dark { left: 630px; top: 140px; }
  .card--back-white { left: 70px; top: 486px; }
  .card--back-dark { left: 630px; top: 486px; }

  .brand {
    position: absolute;
    display: flex;
    align-items: center;
    gap: 8px;
  }
  .brand__square {
    width: 12px; height: 12px;
    background: var(--brand-blue);
  }
  .brand__name {
    color: var(--brand-blue);
    font-weight: 400;
    font-size: 28px;
    letter-spacing: 4px;
    line-height: 1;
  }
  .card__front .brand { left: 26px; top: 120px; }

  .divider {
    position: absolute;
    left: 226px; top: 62px;
    width: 1px; height: 130px;
    background: var(--brand-blue);
  }
  .contact {
    position: absolute;
    left: 240px; top: 64px;
    font-size: 11px;
    line-height: 15px;
  }
  .contact__name {
    color: var(--brand-blue);
    font-size: 19px;
    font-weight: 700;
    line-height: 22px;
  }
  .contact__role { font-size: 10px; margin-bottom: 12px; }
  .contact__line { display: flex; align-items: center; gap: 6px; }
  .contact__line svg { width: 9px; height: 9px; flex: none; }
  .contact__line--plain { padding-left: 15px; }
  .card--white .contact { color: var(--text-dark); }
  .card--white .contact__role { color: var(--muted-dark); }
  .card--dark .contact { color: var(--text-light); }
  .card--dark .contact__role { color: var(--muted-light); }

  .tagline-band {
    position: absolute;
    left: 0; right: 0; top: 236px;
    height: 22px;
    background: linear-gradient(180deg, var(--brand-light) 0%, var(--brand-blue) 100%);
    color: #fff;
    font-size: 12px;
    letter-spacing: 1.5px;
    line-height: 22px;
    padding-left: 40px;
  }
  .tagline-band::after {
    content: "";
    position: absolute;
    left: 0; right: 0; top: 22px;
    height: 6px;
    background: var(--brand-pale);
  }
  .card--dark .tagline-band::after { background: #2a6e8e; }

  .back-mark {
    position: absolute;
    display: flex;
    flex-direction: column;
    align-items: center;
    gap: 10px;
  }
  .back-mark .brand { position: static; }
  .back-mark .brand__name { font-size: 24px; letter-spacing: 4px; }
  .back-mark__web {
    font-size: 11px;
    letter-spacing: 1.5px;
  }
  .card--back-white .back-mark { right: 26px; bottom: 30px; }
  .card--back-white .back-mark__web { color: var(--text-dark); }
  .card--back-dark .back-mark { right: 30px; top: 112px; }
  .card--back-dark .back-mark__web { color: var(--text-light); }
</style>
</head>
<body>

  <section class="card card--white card--front-white card__front" aria-label="Business card front, light">
    <div class="brand"><span class="brand__square"></span><span class="brand__name">KORVANT</span></div>
    <div class="divider"></div>
    <div class="contact">
      <div class="contact__name">Marek Dobrzyn</div>
      <div class="contact__role">Manager</div>
      <div class="contact__line contact__line--plain">ul. Lipowa 17</div>
      <div class="contact__line contact__line--plain">41-806 Harlow, Estovia</div>
      <div class="contact__line">
        <svg viewBox="0 0 10 10"><rect x="3" y="0.5" width="4" height="9" rx="1" fill="none" stroke="#2aa7e0" stroke-width="1.2"/></svg>
        +48 512 34 56 78
      </div>
      <div class="contact__line">
        <svg viewBox="0 0 10 10"><rect x="0.6" y="2" width="8.8" height="6" fill="none" stroke="#2aa7e0" stroke-width="1.1"/><path d="M0.6 2 L5 5.5 L9.4 2" fill="none" stroke="#2aa7e0" stroke-width="1.1"/></svg>
        marek.dobrzyn@korvant.com.pl
      </div>
      <div class="contact__line">
        <svg viewBox="0 0 10 10"><circle cx="5" cy="5" r="4.2" fill="none" stroke="#2aa7e0" stroke-width="1.1"/><path d="M0.8 5 H9.2 M5 0.8 V9.2" stroke="#2aa7e0" stroke-width="0.9"/></svg>
        www.korvant.com.pl
      </div>
    </div>
    <div class="tagline-band">Enabling global capital</div>
  </section>

  <section class="card card--dark card--front-dark card__front" aria-label="Business card front, dark">
    <div class="brand"><span class="brand__square"></span><span class="brand__name">KORVANT</span></div>
    <div class="divider"></div>
    <div class="contact">
      <div class="contact__name">Marek Dobrzyn</div>
      <div class="contact__role">Manager</div>
      <div class="contact__line contact__line--plain">ul. Lipowa 17</div>
      <div class="contact__line contact__line--plain">41-806 Harlow, Estovia</div>
      <div class="contact__line">
        <svg viewBox="0 0 10 10"><rect x="3" y="0.5" width="4" height="9" rx="1" fill="none" stroke="#2aa7e0" stroke-width="1.2"/></svg>
        +48 512 34 56 78
      </div>
      <div class="contact__line">
        <svg viewBox="0 0 10 10"><rect x="0.6" y="2" width="8.8" height="6" fill="none" stroke="#2aa7e0" stroke-width="1.1"/><path d="M0.6 2 L5 5.5 L9.4 2" fill="none" stroke="#2aa7e0" stroke-width="1.1"/></svg>
        marek.dobrzyn@korvant.com.pl
      </div>
      <div class="contact__line">
        <svg viewBox="0 0 10 10"><circle cx="5" cy="5" r="4.2" fill="none" stroke="#2aa7e0" stroke-width="1.1"/><path d="M0.8 5 H9.2 M5 0.8 V9.2" stroke="#2aa7e0" stroke-width="0.9"/></svg>
        www.korvant.com.pl
      </div>
    </div>
    <div class="tagline-band">Enabling global capital</div>
  </section>

  <section class="card card--white card--back-white" aria-label="Business card back, light">
    <div class="back-mark">
      <div class="brand"><span class="brand__square"></span><span class="brand__name">KORVANT</span></div>
      <div class="back-mark__web">www.korvant.com.pl</div>
    </div>
  </section>

  <section class="card card--dark card--back-dark" aria-label="Business card back, dark">
    <div class="back-mark">
      <div class="brand"><span class="brand__square"></span><span class="brand__name">KORVANT</span></div>
      <div class="back-mark__web">www.korvant.com.pl</div>
    </div>
  </section>

</body>
</html>
```